Hip Music Management Co. BIz Card

I have a logo (attached) the back side of the card should the full logo on the entire card- that's it. The front side of the card should show the logo somewhere, keeping with the 4 different shades of blue. The front side of the card can be a white background with logo and colored typeface for all info. Pretty simple.

Target Market(s)

I manage and produce a whole bunch of major label and indie artists.

Industry/Entity Type

Management

Contact Information for Business Card

Velmora Sound House (logo)
Dale Fornwick
President
www.velmorasoundhouse.com
dale@velmorasoundhouse.com
+1 310.555.7182
418 Willow Bend Lane
Ashgrove Falls, NY 10599

Requirements
Must have
• Entire logo on back side. White background on front- unless you provide something more interesting.
Nice to have
• On the front of the card if you choose a white backgound, if possible take my logo without the blue background (over white) that would be cool.

```html
<!DOCTYPE html>
<html lang="en">
<head>
<meta charset="utf-8">
<title>Velmora Sound House – Business Card</title>
<link href="https://fonts.googleapis.com/css2?family=Roboto+Condensed:wght@400;700&family=Roboto:wght@300;400&display=swap" rel="stylesheet">
<style>
  :root {
    --stage-center: #ffffff;
    --stage-edge: #dde3e8;
    --card: #181e48;
    --navy-blue: #0a6db5;
    --teal: #19a9bb;
    --sky: #4ea9e0;
    --name: #1db3c2;
    --title: #6cbbec;
    --detail: #23b2c6;
    --rule: #9aa3c0;
  }
  * { margin: 0; padding: 0; box-sizing: border-box; }
  html, body { width: 1200px; height: 1000px; overflow: hidden; }
  body {
    position: relative;
    background: radial-gradient(ellipse 60% 60% at 50% 50%, var(--stage-center) 0%, #f2f5f7 55%, var(--stage-edge) 100%);
    font-family: "Roboto", Arial, sans-serif;
  }
  .card {
    position: absolute;
    left: 346px;
    width: 544px;
    height: 319px;
    background: var(--card);
    overflow: hidden;
  }
  .card--back { top: 143px; }
  .card--front { top: 529px; }

  .wordmark {
    position: absolute;
    font-family: "Roboto Condensed", "Arial Narrow", sans-serif;
    font-weight: 700;
    color: var(--sky);
    white-space: nowrap;
    letter-spacing: 0.5px;
    text-transform: uppercase;
  }
  .card--back .wordmark {
    left: 0; right: 0;
    top: 133px;
    text-align: center;
    font-size: 44px;
    line-height: 52px;
  }
  .card--front .wordmark {
    left: 239px;
    top: 50px;
    font-size: 21px;
    line-height: 28px;
  }

  .sound-art {
    position: absolute;
    left: 16px;
    top: 131px;
    width: 206px;
    height: 150px;
    background: linear-gradient(to top, var(--navy-blue) 0%, var(--teal) 45%, var(--sky) 100%);
    opacity: 0.85;
  }

  .contact {
    position: absolute;
    left: 237px;
    top: 126px;
    width: 300px;
  }
  .contact__name {
    font-family: "Roboto Condensed", "Arial Narrow", sans-serif;
    font-weight: 700;
    font-size: 22px;
    line-height: 26px;
    color: var(--name);
  }
  .contact__title {
    font-size: 15px;
    line-height: 20px;
    color: var(--title);
  }
  .contact__rule {
    width: 227px;
    height: 1px;
    background: var(--rule);
    margin: 12px 0 5px;
  }
  .contact__list { list-style: none; }
  .contact__list li {
    position: relative;
    padding-left: 13px;
    font-size: 15px;
    line-height: 18.7px;
    font-weight: 300;
    color: var(--detail);
  }
  .contact__list li::before {
    content: "";
    position: absolute;
    left: 1px; top: 8px;
    width: 5px; height: 5px;
    border-radius: 50%;
    background: var(--sky);
  }
</style>
</head>
<body>
  <section class="card card--back" aria-label="Card back">
    <div class="wordmark">Velmora Sound House</div>
  </section>

  <section class="card card--front" aria-label="Card front">
    <div class="wordmark">Velmora Sound House</div>

    <div class="sound-art" role="img" aria-label="Audio level meter graphic in blue and teal tones"></div>

    <div class="contact">
      <div class="contact__name">Dale Fornwick</div>
      <div class="contact__title">President</div>
      <div class="contact__rule"></div>
      <ul class="contact__list">
        <li>www.velmorasoundhouse.com</li>
        <li>dale@velmorasoundhouse.com</li>
        <li>+1 310.555.7182</li>
        <li>418 Willow Bend Lane Ashgrove Falls,<br>NY 10599</li>
      </ul>
    </div>
  </section>
</body>
</html>
```